Urine collection cup with and without sterile seal sticker

Hello. We need a urine cup label designed please with

Name:
Date of Birth:
Date:
Time:
Temp℃:
Specimen ID:

Product code: KTX-58
Volume markings (e.g., 30 mL, 60 mL, 90 mL).
Vesk Lab Checks logo

Could you please provide one version with the additional sterile sticker extending to the top, and one version without the additional sterile sticker?

```html
<!DOCTYPE html>
<html lang="en">
<head>
<meta charset="utf-8">
<title>Vesk Lab Checks – Specimen Cup Labels</title>
<link rel="stylesheet" href="https://fonts.googleapis.com/css2?family=Figtree:wght@400;700;800&display=swap">
<style>
  :root {
    --navy: #2e2983;
    --sky: #2e9cd9;
    --paper: #ffffff;
    --rule: #4a44a0;
  }
  * { box-sizing: border-box; margin: 0; padding: 0; }
  html, body { width: 1200px; height: 1200px; overflow: hidden; background: var(--paper); }
  .canvas { position: relative; width: 1200px; height: 1200px; }

  .label { position: absolute; width: 526px; height: 467px; font-family: "Figtree", sans-serif; color: var(--navy); }
  .label--sealed { left: 56px; top: 351px; }
  .label--plain { left: 626px; top: 352px; }
  .label__shape { position: absolute; left: 0; width: 526px; overflow: visible; }
  .label--sealed .label__shape { top: -169px; height: 636px; }
  .label--plain .label__shape { top: 0; height: 467px; }

  .field { position: absolute; left: 44px; width: 396px; display: flex; align-items: flex-end; height: 24px; font-size: 20px; letter-spacing: -0.2px; }
  .field__name { white-space: nowrap; line-height: 1; }
  .field__line { flex: 1; border-bottom: 1px solid var(--rule); margin-left: 5px; margin-bottom: 3px; }

  .product-code { position: absolute; left: 24px; width: 445px; top: 332px; text-align: center; font-weight: 800; font-size: 22px; }

  .brand { position: absolute; left: 24px; width: 416px; top: 387px; height: 54px; display: flex; align-items: center; justify-content: center; }
  .brand__name { font-family: "Figtree", sans-serif; font-weight: 700; font-size: 23px; color: var(--paper); white-space: nowrap; line-height: 1; }

  .scale__value { position: absolute; left: 470px; width: 58px; text-align: center; font-weight: 700; font-size: 12px; color: var(--paper); }
  .scale__caption { position: absolute; left: 497px; top: 414px; transform: translate(-50%, -50%) rotate(-90deg); font-weight: 700; font-size: 12px; line-height: 1.05; color: var(--paper); text-align: left; white-space: nowrap; }

  .sterile-tab { position: absolute; left: 494px; top: -103px; transform: translate(-50%, -50%) rotate(90deg); font-weight: 800; font-size: 25px; letter-spacing: 0.5px; color: var(--paper); white-space: nowrap; }
</style>
</head>
<body>
<div class="canvas">

  <!-- Label with sterile seal tab -->
  <div class="label label--sealed">
    <svg class="label__shape" viewBox="0 0 526 636" aria-hidden="true">
      <rect x="0" y="169" width="526" height="467" rx="50" fill="var(--navy)"/>
      <path d="M440,636 L440,169 L457,150 L457,12 Q457,0 469,0 L514,0 Q526,0 526,12 L526,586 Q526,636 476,636 Z" fill="var(--sky)"/>
      <rect x="24" y="195" width="445" height="341" rx="16" fill="var(--paper)"/>
      <g stroke="var(--paper)" stroke-width="1.4">
        <line x1="483" x2="516" y1="268" y2="268"/><line x1="483" x2="516" y1="290" y2="290"/>
        <line x1="483" x2="516" y1="312" y2="312"/><line x1="483" x2="516" y1="335" y2="335"/>
        <line x1="483" x2="516" y1="357" y2="357"/>
        <line x1="483" x2="516" y1="408" y2="408"/><line x1="483" x2="516" y1="430" y2="430"/>
        <line x1="483" x2="516" y1="452" y2="452"/><line x1="483" x2="516" y1="475" y2="475"/>
        <line x1="483" x2="516" y1="497" y2="497"/>
      </g>
    </svg>
    <div class="sterile-tab">STERILE</div>

    <div class="field" style="top:59px"><span class="field__name">NAME:</span><span class="field__line"></span></div>
    <div class="field" style="top:100px"><span class="field__name">DATE OF BIRTH:</span><span class="field__line"></span></div>
    <div class="field" style="top:139px"><span class="field__name">DATE:</span><span class="field__line"></span></div>
    <div class="field" style="top:181px"><span class="field__name">TIME:</span><span class="field__line"></span></div>
    <div class="field" style="top:223px"><span class="field__name">TEMP℃:</span><span class="field__line"></span></div>
    <div class="field" style="top:267px"><span class="field__name">SPECIMEN ID:</span><span class="field__line"></span></div>
    <div class="product-code">Product code: KTX-58</div>

    <div class="brand"><span class="brand__name">VESK LAB CHECKS VERIFIED</span></div>

    <div class="scale__value" style="top:66px">90 mL</div>
    <div class="scale__value" style="top:206px">60 mL</div>
    <div class="scale__value" style="top:346px">30 mL</div>
    <div class="scale__caption">Volume<br>markings</div>
  </div>

  <!-- Label without sterile seal tab -->
  <div class="label label--plain">
    <svg class="label__shape" viewBox="0 0 526 467" aria-hidden="true">
      <rect x="0" y="0" width="526" height="467" rx="50" fill="var(--navy)"/>
      <path d="M440,467 L440,0 L476,0 Q526,0 526,50 L526,417 Q526,467 476,467 Z" fill="var(--sky)"/>
      <rect x="24" y="26" width="445" height="341" rx="16" fill="var(--paper)"/>
      <g stroke="var(--paper)" stroke-width="1.4">
        <line x1="483" x2="516" y1="99" y2="99"/><line x1="483" x2="516" y1="121" y2="121"/>
        <line x1="483" x2="516" y1="143" y2="143"/><line x1="483" x2="516" y1="166" y2="166"/>
        <line x1="483" x2="516" y1="188" y2="188"/>
        <line x1="483" x2="516" y1="239" y2="239"/><line x1="483" x2="516" y1="261" y2="261"/>
        <line x1="483" x2="516" y1="283" y2="283"/><line x1="483" x2="516" y1="306" y2="306"/>
        <line x1="483" x2="516" y1="328" y2="328"/>
      </g>
    </svg>

    <div class="field" style="top:59px"><span class="field__name">NAME:</span><span class="field__line"></span></div>
    <div class="field" style="top:100px"><span class="field__name">DATE OF BIRTH:</span><span class="field__line"></span></div>
    <div class="field" style="top:139px"><span class="field__name">DATE:</span><span class="field__line"></span></div>
    <div class="field" style="top:181px"><span class="field__name">TIME:</span><span class="field__line"></span></div>
    <div class="field" style="top:223px"><span class="field__name">TEMP℃:</span><span class="field__line"></span></div>
    <div class="field" style="top:267px"><span class="field__name">SPECIMEN ID:</span><span class="field__line"></span></div>
    <div class="product-code">Product code: KTX-58</div>

    <div class="brand"><span class="brand__name">VESK LAB CHECKS VERIFIED</span></div>

    <div class="scale__value" style="top:66px">90 mL</div>
    <div class="scale__value" style="top:206px">60 mL</div>
    <div class="scale__value" style="top:346px">30 mL</div>
    <div class="scale__caption">Volume<br>markings</div>
  </div>

</div>
</body>
</html>
```